Larkmoor Health- Core Values Graphic for Visual Appeal

I would like a poster that could take these written core values from our organization and create a graphic that we could use for our staff and employees. I would also like to incorporate our branding into this project. Thank you!

Target Market(s)

To helps patients and employees understand the core values of our organization

Industry/Entity Type

Healthcare

Requirements
Must have
• Match our branding
Nice to have
• Please use your creativity!
Should not have
• Overly complex/ busy

```html
<!DOCTYPE html>
<html lang="en">
<head>
<meta charset="utf-8">
<title>Larkmoor Health – Core Values</title>
<link rel="stylesheet" href="https://fonts.googleapis.com/css2?family=Montserrat:wght@900&family=Raleway:wght@800&family=Hind:wght@400;500&family=Fira+Sans:ital,wght@1,400&display=swap">
<style>
  :root {
    --brand-blue: #2fa8e1;
    --ink: #231f20;
    --paper: #f3f3f4;
    --white: #ffffff;
    --rule: #b9b9bb;
    --icon-fill: #dfe4ec;
    --icon-ring: #b8c2d3;
  }
  * { margin: 0; padding: 0; box-sizing: border-box; }
  html, body { width: 884px; height: 1200px; overflow: hidden; }
  body { background: var(--paper); font-family: "Hind", sans-serif; color: var(--ink); }
  .poster { position: relative; width: 884px; height: 1200px; overflow: hidden; background: var(--paper); }

  .header-band { position: absolute; left: 0; top: 0; width: 884px; height: 258px; background: var(--brand-blue); }
  .header-shape { position: absolute; left: 0; top: 0; }

  .brand-mark { position: absolute; left: 61px; top: 128px; width: 240px; text-align: center;
    font-family: "Hind", sans-serif; font-weight: 500; font-size: 26px; line-height: 1.1; color: var(--ink); }
  .brand-dot { display: block; width: 22px; height: 22px; border-radius: 50%; background: var(--brand-blue); margin: 0 auto 10px; }

  .title { position: absolute; right: 42px; font-family: "Montserrat", sans-serif; font-weight: 900; line-height: 1; letter-spacing: -2px; }
  .title-core { top: 14px; font-size: 128px; color: var(--white); }
  .title-values { top: 128px; font-size: 118px; color: var(--ink); }

  .intro { position: absolute; left: 42px; top: 302px; width: 800px; font-family: "Fira Sans", sans-serif; font-style: italic;
    font-size: 16.4px; line-height: 20px; color: var(--ink); }
  .intro em { color: var(--brand-blue); font-style: italic; }

  .value-chain { position: absolute; left: 46px; top: 388px; }

  .value { position: absolute; left: 270px; width: 572px; }
  .value h2 { font-family: "Raleway", sans-serif; font-weight: 800; font-size: 37px; line-height: 1; letter-spacing: -0.3px; margin-bottom: 10px; }
  .value h2.blue { color: var(--brand-blue); }
  .value p { font-size: 14.2px; line-height: 17.8px; text-align: justify; hyphens: auto; }
  .value-family { top: 392px; }
  .value-excellence { top: 582px; }
  .value-integrity { top: 792px; }
  .value-service { top: 988px; }

  .divider { position: absolute; left: 271px; width: 570px; height: 1.5px; background: var(--rule); }

  .footer-pill { position: absolute; left: 201px; top: 1146px; width: 481px; height: 60px; background: var(--brand-blue);
    border-radius: 30px 30px 0 0; color: var(--white); text-align: center; padding-top: 15px;
    font-family: "Hind", sans-serif; font-size: 16px; letter-spacing: 3.6px; }
  .footer-pill b { font-weight: 500; }
</style>
</head>
<body>
<main class="poster">
  <div class="header-band"></div>
  <svg class="header-shape" width="884" height="300" viewBox="0 0 884 300">
    <path d="M0 0 L160 0 C190 25 230 40 280 55 C330 75 345 120 330 160 L60 160 C40 140 20 125 0 120 Z" fill="#ffffff"/>
    <path d="M0 150 C40 145 70 175 80 230" fill="none" stroke="#ffffff" stroke-width="3"/>
    <circle cx="181" cy="158" r="126" fill="#ffffff" stroke="#2fa8e1" stroke-width="8"/>
  </svg>
  <div class="brand-mark"><span class="brand-dot"></span>Larkmoor Health</div>

  <div class="title title-core">CORE</div>
  <div class="title title-values">VALUES</div>

  <p class="intro">These <em>core values</em> are the spirit of who we are as a healthcare team. They guide our actions, unite us in purpose, and ensure that we provide world-class care while fostering a positive and supportive atmosphere within our team:</p>

  <svg class="value-chain" width="150" height="760" viewBox="0 0 150 760">
    <rect x="45" y="60" width="60" height="620" fill="#2fa8e1"/>
    <circle cx="75" cy="75" r="75" fill="#2fa8e1"/>
    <circle cx="75" cy="273" r="75" fill="#2fa8e1"/>
    <circle cx="75" cy="470" r="75" fill="#2fa8e1"/>
    <circle cx="75" cy="669" r="75" fill="#2fa8e1"/>
    <circle cx="75" cy="75" r="57" fill="#dfe4ec" stroke="#b8c2d3" stroke-width="3" role="img" aria-label="Family icon"/>
    <circle cx="75" cy="273" r="57" fill="#dfe4ec" stroke="#b8c2d3" stroke-width="3" role="img" aria-label="Excellence icon: thumbs up with stars"/>
    <circle cx="75" cy="470" r="57" fill="#dfe4ec" stroke="#b8c2d3" stroke-width="3" role="img" aria-label="Integrity icon: puzzle pieces with gear"/>
    <circle cx="75" cy="669" r="57" fill="#dfe4ec" stroke="#b8c2d3" stroke-width="3" role="img" aria-label="Service icon: gear and wrench"/>
  </svg>

  <section class="value value-family">
    <h2 class="blue">FAMILY</h2>
    <p>At the heart of our mission is the commitment to provide high-quality, affordable healthcare in a comforting and uplifting family-oriented environment. Just as our community is our extended family, every patient is a cherished member of our healthcare family. We treat each individual with the same care, compassion, and respect we would offer to our own loved ones.</p>
  </section>
  <div class="divider" style="top:551px"></div>

  <section class="value value-excellence">
    <h2>EXCELLENCE</h2>
    <p>In line with our goal, we aspire not only to alleviate pain but also to inspire patients to become active participants in their well-being. We believe in empowering our patients through education and compassion. Our pursuit of excellence is unwavering, driven by our dedication to continuously improve our services at every level, ensuring that our community receives nothing less than exceptional care.</p>
  </section>
  <div class="divider" style="top:760px"></div>

  <section class="value value-integrity">
    <h2 class="blue">INTEGRITY</h2>
    <p>In our healthcare team, 'Integrity' is non-negotiable. Our purpose is deeply rooted in ethics, integrity, and professional standards. We operate with the utmost integrity in every aspect of our work, adhering to the highest ethical principles. We understand that trust is the foundation of healthcare, and we are committed to maintaining the trust our community places in us.</p>
  </section>
  <div class="divider" style="top:958px"></div>

  <section class="value value-service">
    <h2>SERVICE</h2>
    <p>Our vision is grounded in the belief that every person possesses the innate potential for true health. We aim to facilitate the body's natural healing response by providing the highest level of service. Our hope for each patient extends beyond healing; we aspire to help you fulfill your life's mission and purpose abundantly, supporting you in your journey to well-being.</p>
  </section>

  <footer class="footer-pill">WWW.<b>LARKMOORHEALTH</b>.COM</footer>
</main>
</body>
</html>
```